Web design for sitter site

We will be launching a sitter site in the coming months that focuses on sitters for children. The name of this site will be KidHaven.com
We will need:
1. main page design
2. site logo designed
3. subpages as well for the look of people's profiles, and job listings, etc (see links below)
We only need the design, photos, font files, etc. We do not need this site coded (no html), a ps job is fine.
Some competing sites in the space include - tendlyhub.com and vurl.com
http://www.brisk-minder.example/images/profile1.jpg
http://quenthollibrary.example/wp-content/uploads/2013/09/vurl-review.png
http://www.palvermont.example/hr/photos/tendly_hub2.jpg
Target Market(s)
Mothers of children, mainly women
Industry/Entity Type
Online
Look and feel

```html
<!DOCTYPE html>
<html lang="en">
<head>
<meta charset="utf-8">
<title>KidHaven – Find better care for your whole family</title>
<link href="https://fonts.googleapis.com/css2?family=Open+Sans:wght@400;600&display=swap" rel="stylesheet">
<style>
:root{
  --sky:#4bb9df;
  --sky-light:#6cc6e6;
  --ink:#2b2b25;
  --text:#333;
  --header-bg:#f9f8f6;
  --line:#e6e6e6;
  --yellow:#ffc10e;
  --green:#7cc414;
  --dark:#3e3e3e;
  --footer:#454545;
}
*{margin:0;padding:0;box-sizing:border-box}
html,body{width:750px;height:1200px;overflow:hidden;background:#fff}
body{position:relative;font-family:"Open Sans",Arial,sans-serif;color:var(--text)}
.abs{position:absolute}

.site-header{left:0;top:0;width:750px;height:82px;background:var(--header-bg)}
.brand{left:112px;top:26px;font-size:22px;font-weight:400;color:var(--sky);letter-spacing:.5px}
.contact-info{left:554px;top:26px;display:flex;gap:9px;align-items:center}
.contact-info p{font-size:10px;line-height:20px;color:var(--ink)}

.main-nav{left:0;top:82px;width:750px;height:32px;background:var(--sky);border-bottom:2px solid #3a4a4f}
.main-nav a{position:absolute;top:10px;font-size:8px;color:#fff;text-decoration:none}

.hero{left:0;top:114px;width:750px;height:342px}
.hero-photo{width:100%;height:100%;background:linear-gradient(90deg,#eef1f2 0%,#e3e8ea 45%,#d9cbbf 70%,#e8e6e4 100%)}
.hero-title{left:113px;top:176px;font-size:23.5px;font-weight:600;line-height:41px;color:var(--ink)}
.hero-dots{left:113px;top:317px;display:flex;gap:5px}
.hero-dots span{width:7px;height:7px;border-radius:50%;background:#2c2c2c}
.hero-dots span.active{background:var(--sky);box-shadow:0 0 0 1px #fff}

.get-started{left:114px;top:382px;width:523px;height:176px;background:linear-gradient(180deg,var(--sky-light),#5dbde2);border:2px solid #fff;box-shadow:0 8px 10px -6px rgba(0,0,0,.35)}
.get-started h2{position:absolute;top:15px;width:100%;text-align:center;font-size:15px;font-weight:600;color:#fff}
.option{position:absolute;top:49px;width:226px;height:105px;background:linear-gradient(180deg,#fff 40%,#eef3f5);text-align:center}
.option h3{margin-top:11px;font-size:13.5px;font-weight:600;color:var(--ink)}
.option h3 em{font-style:normal;color:var(--sky)}
.option p{margin-top:7px;font-size:9.5px;color:var(--ink)}
.option .btn{display:inline-block;margin-top:9px;width:78px;height:27px;line-height:27px;background:var(--sky);color:#fff;font-size:13.5px}

.service{top:584px;width:166px;height:218px;border:1px solid var(--line);text-align:center}
.service .thumb{margin:3px;height:93px}
.service h3{margin-top:13px;font-size:11px;font-weight:400;color:var(--ink)}
.service p{margin:13px 8px 0;font-size:6.4px;line-height:12px;color:var(--text)}
.service .more{position:absolute;left:63px;bottom:5px;width:42px;height:18px;border-radius:21px 21px 0 0;color:#fff;font-size:7.5px;line-height:20px}
.service .bar{position:absolute;left:-1px;right:-1px;bottom:-1px;height:7px}

.section-title{top:818px;font-size:13.5px;font-weight:400;color:var(--ink);width:257px;padding-bottom:9px;border-bottom:1px solid #eee}
.section-title em{font-style:normal;color:var(--sky)}

.welcome-photo{left:112px;top:861px;width:244px;height:118px;border:1px solid var(--line);padding:2px}
.welcome-photo div{width:100%;height:100%;background:linear-gradient(90deg,#eceef0,#e2c2a6 50%,#f2eeea)}
.welcome-title{left:112px;top:993px;font-size:13px;font-weight:400;color:var(--ink)}
.welcome-text{left:112px;top:1022px;width:248px;font-size:6.3px;line-height:11.8px;color:var(--text)}
.learn-more{left:113px;top:1097px;width:61px;height:23px;line-height:23px;text-align:center;background:var(--dark);color:#fff;font-size:7.5px;border-radius:2px}

.news-item{left:381px;width:258px;height:116px;border:1px solid var(--line);background:#fafafa}
.news-item .thumb{position:absolute;left:11px;top:11px;width:86px;height:80px;border:1px solid var(--line);padding:2px;background:#fff}
.news-item .thumb div{width:100%;height:100%}
.news-item h4{position:absolute;left:109px;top:10px;font-size:9.5px;font-weight:400;color:var(--ink)}
.news-item time{position:absolute;left:109px;top:32px;font-size:6.5px;color:var(--ink)}
.news-item p{position:absolute;left:109px;top:47px;width:136px;font-size:6.4px;line-height:11.8px;text-align:justify;color:var(--text)}
.news-item .read{position:absolute;right:13px;top:97px;font-size:6.5px;color:var(--sky)}

.site-footer{left:0;top:1142px;width:750px;height:58px;background:var(--footer);border-top:2px solid var(--sky)}
.footer-links{position:absolute;left:113px;top:15px;font-size:7px;color:#eee}
.copyright{position:absolute;left:112px;top:34px;font-size:7px;color:#ddd}
.social{position:absolute;left:570px;top:22px;display:flex;gap:6px}
.social span{width:13px;height:13px;border-radius:50%;background:#f2f2f2}
</style>
</head>
<body>

<header class="site-header abs">
  <div class="brand abs">KidHaven</div>
  <div class="contact-info abs">
    <svg width="15" height="27" viewBox="0 0 15 27" aria-hidden="true"><rect x="1" y="1" width="13" height="25" rx="2" fill="none" stroke="#111" stroke-width="2"/><rect x="3" y="5" width="9" height="15" fill="#111"/><circle cx="7.5" cy="23" r="1.2" fill="#111"/></svg>
    <p>Call For Info<br>555 014 2290</p>
  </div>
</header>

<nav class="main-nav abs">
  <a style="left:112px">What We Offer</a>
  <a style="left:203px">Child Care</a>
  <a style="left:277px">Senior Care</a>
  <a style="left:350px">Pet Care</a>
  <a style="left:408px">How it works</a>
  <a style="left:484px">Date Night</a>
  <a style="left:556px">Contact Us</a>
</nav>

<section class="hero abs">
  <div class="hero-photo" role="img" aria-label="Smiling young caregiver in a bright, softly blurred home interior"></div>
</section>
<h1 class="hero-title abs">We're making it easier to<br>find better care for your<br>whole family</h1>
<div class="hero-dots abs"><span class="active"></span><span></span><span></span></div>

<section class="get-started abs">
  <h2>Let's get started. choose an option.</h2>
  <div class="option" style="left:16px">
    <h3>I need a <em>caregiver</em></h3>
    <p>Start your free search for care in your area.</p>
    <span class="btn">Find Care</span>
  </div>
  <div class="option" style="left:257px">
    <h3>I want a care <em>job</em></h3>
    <p>Create a free profile and search for jobs.</p>
    <span class="btn">Find Jobs</span>
  </div>
</section>

<article class="service abs" style="left:112px">
  <div class="thumb" role="img" aria-label="Father holding his baby" style="background:linear-gradient(90deg,#eceae6,#d9c2ae,#eceae6)"></div>
  <h3>Sitters for Children</h3>
  <p>Praesent vestibulum molestie lacus. Aenean nonummy hendrerit mauris. Phasellus porta. Fusce suscipit varius mi. Cum sociis natoque penatibus et magnis.</p>
  <span class="more" style="background:var(--sky)">More</span>
  <span class="bar" style="background:var(--sky)"></span>
</article>
<article class="service abs" style="left:292px">
  <div class="thumb" role="img" aria-label="Small spaniel on a leash in green grass" style="background:linear-gradient(180deg,#5f8c3a,#7fae3e 60%,#6a9a2c)"></div>
  <h3>Pet care</h3>
  <p>Praesent vestibulum molestie lacus. Aenean nonummy hendrerit mauris. Phasellus porta. Fusce suscipit varius mi. Cum sociis natoque penatibus et magnis.</p>
  <span class="more" style="background:var(--yellow)">More</span>
  <span class="bar" style="background:var(--yellow)"></span>
</article>
<article class="service abs" style="left:472px">
  <div class="thumb" role="img" aria-label="Caregiver with an elderly man" style="background:linear-gradient(90deg,#d8c0a8,#eef0f2,#b9c9dc)"></div>
  <h3>Elderly Care</h3>
  <p>Praesent vestibulum molestie lacus. Aenean nonummy hendrerit mauris. Phasellus porta. Fusce suscipit varius mi. Cum sociis natoque penatibus et magnis.</p>
  <span class="more" style="background:var(--green)">More</span>
  <span class="bar" style="background:var(--green)"></span>
</article>

<h2 class="section-title abs" style="left:112px;width:244px">Welcome To <em>KidHaven</em></h2>
<h2 class="section-title abs" style="left:381px">News &amp; <em>Events</em></h2>

<div class="welcome-photo abs"><div role="img" aria-label="Mother and daughter hugging"></div></div>
<h3 class="welcome-title abs">Sitters for Children</h3>
<p class="welcome-text abs">Aenean placerat tortor ac dui luctus ut mattis est mollis. Donec blandit orci id velit cursus varius. Fusce quam enim, hendrerit nec ultrices a, vestibulum nec enim. Quisque imperdiet ultricies dolor in convallis. Morbi sed fringilla elit. Duis sagittis lectus in orci volutpat elementum. Cras in purus sem. Curabitur augue velit, mollis in suscipit eleifend, faucibus ac elit. Morbi mattis tristique mi,</p>
<span class="learn-more abs">Learn More</span>

<article class="news-item abs" style="top:862px">
  <div class="thumb"><div role="img" aria-label="Senior couple smiling together" style="background:linear-gradient(90deg,#e7dccf,#d6b9a0,#eee8e0)"></div></div>
  <h4>Adult and senior care</h4>
  <time>March-22-2011</time>
  <p>Lorem ipsum dolor sit amet, consectetuer adipiscing elit, sed diam nonummy nibh euismod tincidunt ut laoreet dolore magna aliquam erat volutpat.</p>
  <span class="read">Read More</span>
</article>
<article class="news-item abs" style="top:994px">
  <div class="thumb"><div role="img" aria-label="Boy holding a small spaniel puppy" style="background:linear-gradient(135deg,#4d8ac0,#c79a64 55%,#5d9a3c)"></div></div>
  <h4>Boy With Pet King Charles</h4>
  <time>March-22-2011</time>
  <p>Lorem ipsum dolor sit amet, consectetuer adipiscing elit, sed diam nonummy nibh euismod tincidunt ut laoreet dolore magna aliquam erat volutpat.</p>
  <span class="read">Read More</span>
</article>

<footer class="site-footer abs">
  <div class="footer-links">Home &nbsp;|&nbsp; Safety Center &nbsp;|&nbsp; Pictures &nbsp;|&nbsp; Location &nbsp;|&nbsp; Contact Us</div>
  <div class="copyright">©2014 kidhaven.com, All Rights Reserved.</div>
  <div class="social" aria-label="Social links"><span></span><span></span><span></span><span></span></div>
</footer>

</body>
</html>
```